Brochure for Law Support Services Company

Hi
I need a 2-fold brochure for my small company. We provide office services for law firms in Brazil. The company website is this one: www.vtamplexo.com.br
A law firm can have an internal admin team that does all bureaucratic/official work at tribunals.  These services range from lawsuits copies, certification, registrar and we also perform official duties like representing law firms in judgements. It is costly for customers to do this in-house as they lack scale and expertise.
My company offer outsource this services, with the following advantages:
1) We offer countrywide coverage
2) Customers can order and follow their service online
3) We have agreed pre-defined prices
4) We guarantee timeliness and accuracy
We achieve this thru 3 pillars: expertise, process and technology.
I need a brochure that has some basic sessions, describing our services, how we work and the value we provide. You dont need to write in Portuguese, but I need the structure so I can fill the gaps with text.
For example, I need a Brazilian map showing our coverage, the 3 pillars, an area for a case study, a session that shows our value prop.
Thanks
Nelo

Target Market(s)
Law firms
Industry/Entity Type
Law Firm
Requirements
Must have
- Professional - example attached
Logo attached
If someone make me one like the one I attached it will have higher chance to win (instead of Australia map) I need a brazilian on the same look/feel
Should not have
- Casual look

```html
<!DOCTYPE html>
<html lang="en">
<head>
<meta charset="utf-8">
<title>Vtamplexo Legal – Brochure Spreads</title>
<link rel="stylesheet" href="https://fonts.googleapis.com/css2?family=Ubuntu:wght@400;500;700&family=Arimo:wght@400;700&display=swap">
<style>
  :root{
    --magenta:#8c1d58;
    --magenta-soft:#b05a86;
    --grey:#707072;
    --grey-light:#a7a7a9;
    --grey-pale:#ececec;
    --black:#1f1f1f;
    --paper:#ffffff;
    --backdrop:#d4d4d6;
    --head:"Ubuntu",sans-serif;
    --body:"Arimo",sans-serif;
  }
  *{box-sizing:border-box;margin:0;padding:0}
  html,body{width:1200px;height:1000px;overflow:hidden}
  body{background:var(--backdrop);position:relative;font-family:var(--body)}
  .spread{position:absolute;left:268px;width:664px;height:470px;display:flex;box-shadow:0 6px 18px rgba(0,0,0,.25)}
  .spread--inside{top:20px}
  .spread--outside{top:510px}
  .page{position:relative;width:332px;height:470px;background:var(--paper);overflow:hidden}
  .page + .page{border-left:1px solid #dcdcdc}
  .bar{position:absolute}
  .bar--grey{background:var(--grey-light)}
  .bar--dark{background:var(--grey)}
  .bar--black{background:var(--black)}
  .bar--pale{background:var(--grey-pale)}

  .section-title{position:absolute;font-family:var(--head);font-size:17px;color:var(--grey);font-weight:400}
  .section-title em{font-style:normal;color:var(--magenta)}
  .title-rule{position:absolute;height:1px;background:var(--grey)}
  .title-rule::after{content:"";position:absolute;left:14px;top:0;border-left:5px solid transparent;border-right:5px solid transparent;border-top:6px solid var(--black)}

  .value-copy{position:absolute;left:32px;top:66px;width:196px;color:var(--magenta);font-size:7.6px;line-height:1.35}
  .value-copy p{margin-bottom:8px}
  .side-list{position:absolute;left:236px;top:32px;width:90px;color:var(--magenta-soft);font-size:7.2px;line-height:1.4;list-style:none}
  .side-list li{white-space:nowrap}
  .side-list li::before{content:"*"}
  .side-list .gap{margin-top:22px}

  .photo{position:absolute}
  .photo--paper{background:linear-gradient(135deg,#eef2f5,#9fb0bf)}
  .photo--globe{background:radial-gradient(circle at 55% 50%,#3f6f96,#c9dbe8 70%)}
  .photo--office{background:linear-gradient(160deg,#5c6e80,#27313b)}
  .photo--library{background:linear-gradient(160deg,#b07a35,#4a2a12)}
  .photo--tower{background:linear-gradient(160deg,#9bb7d4,#2d3a47)}
  .photo--pen{background:linear-gradient(150deg,#d9cbb4,#7a6a56)}
  .photo-label{position:absolute;left:0;right:0;top:6px;text-align:center;font-family:var(--head);font-size:13px;color:#fff;text-shadow:0 1px 2px rgba(0,0,0,.5)}

  .tile-text{position:absolute;color:#fff;font-size:6.8px;line-height:1.35;padding:5px 6px}
  .tile-text--grey{background:var(--grey)}
  .tile-text--magenta{background:var(--magenta)}

  .map-area{position:absolute;left:112px;top:48px;width:140px;height:122px;border-radius:30% 40% 45% 25% / 30% 35% 55% 40%;background:radial-gradient(circle at 50% 45%,#b15a88,#8c1d58 75%)}
  .map-lines{position:absolute;left:0;top:0}
  .map-note{position:absolute;font-size:6.2px;color:var(--magenta);white-space:nowrap}

  .services{position:absolute;left:28px;top:24px;width:292px;height:310px;background:var(--magenta);color:#fff}
  .services .section-title{left:12px;top:8px;color:#fff}
  .services .title-rule{background:#fff;left:12px;top:30px;width:120px}
  .services .title-rule::after{border-top-color:#fff}
  .service-col{position:absolute;top:42px;width:128px;font-size:7.2px;line-height:1.35;list-style:none}
  .service-col li::before{content:"*"}
  .service-col .gap{margin-top:14px}
  .back-strip{position:absolute;left:28px;top:340px;width:292px;height:44px;background:var(--grey);color:#fff;font-size:7.4px;line-height:1.4;text-align:center;padding:7px 12px}

  .cover-band{position:absolute;left:30px;top:246px;width:302px;height:62px;background:var(--magenta);color:#fff;font-family:var(--head);font-size:12.5px;line-height:1.55;text-align:right;padding:12px 14px 0 0;letter-spacing:.2px}

  .brand{position:absolute;display:flex;align-items:center;gap:6px}
  .brand-mark{width:14px;height:14px;background:var(--grey)}
  .brand-name{font-family:var(--head);font-weight:500;color:var(--magenta);letter-spacing:.5px}
  .brand-tag{position:absolute;font-size:6.6px;color:var(--grey)}
</style>
</head>
<body>

<section class="spread spread--inside">
  <article class="page page--value">
    <div class="bar bar--grey" style="left:0;top:22px;width:14px;height:200px"></div>
    <div class="bar bar--black" style="left:0;top:228px;width:14px;height:190px"></div>

    <h2 class="section-title" style="left:32px;top:30px"><em>Our</em> Value</h2>
    <div class="title-rule" style="left:32px;top:53px;width:200px"></div>

    <div class="value-copy">
      <p>Attachment apartments in delightful by motionless it no. And now she burst sir learn total. Hearing hearted shewing own ask. Solicitude uncommonly use her motionless not collecting age. The properly servants.</p>
      <p>Required mistaken outlived bed and. Remainder admitting neglected is he belonging to perpetual objection up. Has widen too you decay begin which asked equal any.</p>
      <p>Attachment apartments in delightful by motionless it no. And now she burst sir learn total. Hearing hearted shewing own ask. Solicitude uncommonly use her motionless not collecting age.</p>
    </div>

    <ul class="side-list">
      <li>Far concluded not</li>
      <li>his something</li>
      <li>extremity. Want four</li>
      <li>we face an he gate.</li>
      <li>On he of played he</li>
      <li class="gap">ladies answer little</li>
      <li>though nature.</li>
      <li>Blessing oh do</li>
      <li>pleasure as so</li>
      <li>formerly.</li>
    </ul>

    <div class="photo photo--paper" role="img" aria-label="Photo of stacked legal documents" style="left:24px;top:248px;width:98px;height:66px"></div>
    <div class="photo photo--paper" role="img" aria-label="Photo of a business contract and pen" style="left:126px;top:248px;width:98px;height:66px"></div>
    <div class="photo photo--globe" role="img" aria-label="Photo of a glass globe" style="left:228px;top:248px;width:98px;height:66px"></div>

    <div class="tile-text tile-text--grey" style="left:24px;top:317px;width:98px;height:104px">Insensible possession oh particular attachment at excellence in. The books arose but miles happy she. It building contempt or interest children mistress of unlocked. Collecting she contained mrs led listening resembled.</div>
    <div class="tile-text tile-text--magenta" style="left:126px;top:317px;width:98px;height:84px">Unpleasant astonished an diminution up partiality. Noisy an their of meant. Death means up civil do an offer wound of. Called square an in afraid direct. Resolution diminution so mr at unpleasing simplicity no.</div>
    <div class="tile-text tile-text--grey" style="left:228px;top:317px;width:98px;height:124px">No twenty spring of in esteem spirit likely estate. Continue new you declared differed learning bringing honoured. At mean mind so upon they rent am walk. Shortly am waiting inhabit smiling he chiefly of in. Lain tore time gone him his dear sure. Fat decisively estimating affronting assistance not.</div>
  </article>

  <article class="page page--work">
    <h2 class="section-title" style="left:20px;top:30px"><em>Our</em> Work</h2>
    <div class="title-rule" style="left:20px;top:53px;width:110px"></div>

    <div class="map-area" role="img" aria-label="Dotted map of Brazil showing national coverage"></div>
    <svg class="map-lines" width="332" height="200" viewBox="0 0 332 200" aria-hidden="true">
      <g stroke="#707072" stroke-width="0.6" fill="none">
        <polyline points="240,62 246,58 318,58"/>
        <polyline points="130,110 100,124 28,124"/>
        <polyline points="170,150 150,168 95,168"/>
        <polyline points="232,128 252,140 318,140"/>
      </g>
    </svg>
    <span class="map-note" style="left:238px;top:49px">few estimating men favourable</span>
    <span class="map-note" style="left:28px;top:115px">formerly calling an unpacked</span>
    <span class="map-note" style="left:95px;top:170px">sentiments simplicity</span>
    <span class="map-note" style="left:270px;top:131px">uneasy removal</span>

    <div class="bar bar--pale" style="left:0;top:186px;width:332px;height:12px"></div>
    <div class="bar bar--black" style="left:318px;top:186px;width:14px;height:196px"></div>

    <div class="photo photo--office" role="img" aria-label="Photo of business people at work" style="left:10px;top:198px;width:98px;height:70px"><span class="photo-label">Process</span></div>
    <div class="photo photo--library" role="img" aria-label="Photo of an open law book in a library" style="left:112px;top:198px;width:98px;height:70px"><span class="photo-label">Expertise</span></div>
    <div class="photo photo--tower" role="img" aria-label="Photo of a glass office tower" style="left:214px;top:198px;width:98px;height:70px"><span class="photo-label">Technology</span></div>

    <div class="tile-text tile-text--grey" style="left:10px;top:271px;width:98px;height:96px">Remain valley who mrs uneasy remove wooded him you. Her questions favourite him concealed. We to wife face took he. The taste begin early old why since dried can first. Prepared as or humoured formerly. Evil mrs true get post.</div>
    <div class="tile-text tile-text--magenta" style="left:112px;top:271px;width:98px;height:80px">Delightful unreserved impossible few estimating men favourable see entreaties. She propriety immediate was improving. He or entrance humoured likewise moderate. Much nor game son say feel.</div>
    <div class="tile-text tile-text--grey" style="left:214px;top:271px;width:98px;height:84px">Written enquire painful ye to offices forming it. Then so does over sent dull on. Likewise offended humoured mrs fat trifling answered. On ye position greatest so desirous.</div>
  </article>
</section>

<section class="spread spread--outside">
  <article class="page page--back">
    <div class="bar bar--grey" style="left:0;top:24px;width:20px;height:70px"></div>
    <div class="bar bar--black" style="left:0;top:250px;width:20px;height:134px"></div>

    <div class="services">
      <h2 class="section-title"><em style="color:#fff">Our</em> Services</h2>
      <div class="title-rule"></div>
      <ul class="service-col" style="left:12px">
        <li>Affronting discretion as do is announcing.</li>
        <li>Now months esteem oppose nearer enable</li>
        <li>too six. She numerous unlocked you perceive speedily.</li>
        <li>Affixed offence spirits or ye of offices between.</li>
        <li>Real on shot it were four an as. Absolute bachelor rendered six nay you juvenile.</li>
        <li>Vanity entire an chatty to.</li>
        <li class="gap">Affronting discretion as do is announcing.</li>
        <li>Now months esteem oppose nearer enable</li>
        <li>too six. She numerous unlocked you perceive speedily.</li>
        <li>Affixed offence spirits or ye of offices between.</li>
        <li>Real on shot it were four an as. Absolute bachelor rendered six nay you juvenile.</li>
        <li>Vanity entire an chatty to.</li>
      </ul>
      <ul class="service-col" style="left:152px;top:20px">
        <li>Affronting discretion as do is announcing.</li>
        <li>Now months esteem oppose nearer enable</li>
        <li>too six. She numerous unlocked you perceive speedily.</li>
        <li>Affixed offence spirits or ye of offices between.</li>
        <li>Real on shot it were four an as. Absolute bachelor rendered six nay you juvenile.</li>
        <li>Vanity entire an chatty to.</li>
        <li class="gap">Affronting discretion as do is announcing.</li>
        <li>Now months esteem oppose nearer enable</li>
        <li>too six. She numerous unlocked you perceive speedily.</li>
        <li>Affixed offence spirits or ye of offices between.</li>
      </ul>
    </div>

    <div class="back-strip">Started earnest brother believe an exposed so. Me he believing daughters if forfeited at furniture. Age again and stuff downs spoke. Late hour new nay able fat each sell.</div>

    <div class="brand" style="left:28px;top:412px">
      <span class="brand-mark"></span>
      <span class="brand-name" style="font-size:13px">VTAMPLEXO LEGAL</span>
    </div>
    <span class="brand-tag" style="left:48px;top:430px">Serviços de Advocacia de Apoio</span>
  </article>

  <article class="page page--cover">
    <div class="bar bar--grey" style="left:0;top:24px;width:12px;height:110px"></div>
    <div class="bar bar--black" style="left:0;top:140px;width:12px;height:120px"></div>
    <div class="bar bar--grey" style="left:0;top:300px;width:12px;height:60px"></div>

    <div class="photo photo--pen" role="img" aria-label="Photo of a fountain pen resting on a handwritten manuscript" style="left:30px;top:24px;width:290px;height:218px"></div>

    <div class="cover-band">Difficulty on insensible<br>reasonable in. From as went he they</div>

    <div class="brand" style="left:150px;top:378px">
      <span class="brand-mark"></span>
      <span class="brand-name" style="font-size:15px">VTAMPLEXO LEGAL</span>
    </div>
    <span class="brand-tag" style="left:170px;top:399px;font-size:7.4px">Serviços de Advocacia de Apoio</span>
  </article>
</section>

</body>
</html>
```